Landscaping business card

We need a business card that reflects our business. We do lawncare and landscaping with all natural materials and have a great track record in the communities we serve: Newton, Brookline, Wellesley, Brighton, Watertown, and Waltham. We have been in business for 10 years.
Updates

I don't know the curvy fonts. Please keep the fonts fairly conservative.

Industry/Entity Type

Landscaping

Contact Information for Business Card

Harrowgate Landscaping
Marc Harrowgate
Founder and CEO
918 Pinchot Rd
Larkfield, NH 02913

Requirements
Must have
• The color green

```html
<!DOCTYPE html>
<html lang="en">
<head>
<meta charset="utf-8">
<title>Harrowgate Landscaping Business Card</title>
<link rel="stylesheet" href="https://fonts.googleapis.com/css2?family=Oswald:wght@700&family=Arimo:wght@400;700&display=swap">
<style>
  :root {
    --backdrop-light: #a3a3a3;
    --backdrop-dark: #6f6f6f;
    --grass-light: #6cbb2e;
    --grass-mid: #3f8a1a;
    --grass-deep: #24600f;
    --band-tint: rgba(20, 70, 10, 0.45);
    --band-edge: rgba(200, 240, 170, 0.35);
    --ink: #ffffff;
  }
  html, body {
    margin: 0;
    width: 1200px;
    height: 861px;
    overflow: hidden;
  }
  body {
    background: radial-gradient(ellipse at 50% 35%, var(--backdrop-light), var(--backdrop-dark));
    display: flex;
    align-items: center;
    justify-content: center;
  }
  .business-card {
    position: relative;
    width: 840px;
    height: 480px;
    overflow: hidden;
    box-shadow: 0 14px 30px rgba(0, 0, 0, 0.35);
  }
  .grass-photo {
    position: absolute;
    inset: 0;
    background: linear-gradient(180deg, var(--grass-light) 0%, var(--grass-mid) 45%, var(--grass-deep) 78%, var(--grass-deep) 100%);
  }
  .title-band {
    position: absolute;
    left: 0;
    right: 0;
    top: 92px;
    height: 96px;
    background: var(--band-tint);
    border-top: 2px solid var(--band-edge);
    border-bottom: 2px solid var(--band-edge);
    display: flex;
    align-items: center;
    justify-content: center;
  }
  .company-name {
    margin: 0;
    font-family: "Oswald", "Arial Narrow", sans-serif;
    font-weight: 700;
    font-size: 58px;
    letter-spacing: 1px;
    text-transform: uppercase;
    color: var(--ink);
    line-height: 1;
    white-space: nowrap;
  }
  .person {
    position: absolute;
    left: 190px;
    top: 208px;
    color: var(--ink);
    font-family: "Arimo", Arial, sans-serif;
  }
  .person-name {
    margin: 0;
    font-weight: 700;
    font-size: 50px;
    line-height: 1.05;
  }
  .person-role {
    margin: 2px 0 0 66px;
    font-weight: 400;
    font-size: 27px;
  }
  .address {
    position: absolute;
    left: 52px;
    top: 364px;
    display: flex;
    align-items: center;
    gap: 14px;
    color: var(--ink);
    font-family: "Arimo", Arial, sans-serif;
    font-size: 33px;
    white-space: nowrap;
  }
  .pin-icon {
    width: 44px;
    height: 44px;
    flex: none;
  }
</style>
</head>
<body>
  <div class="business-card">
    <div class="grass-photo" role="img" aria-label="Close-up photograph of a lush green lawn"></div>
    <div class="title-band">
      <h1 class="company-name">Harrowgate Landscaping</h1>
    </div>
    <div class="person">
      <p class="person-name">Marc Harrowgate</p>
      <p class="person-role">Founder and CEO</p>
    </div>
    <div class="address">
      <svg class="pin-icon" viewBox="0 0 44 44" aria-hidden="true">
        <circle cx="22" cy="22" r="22" fill="#ffffff"/>
        <path d="M22 9c-5.5 0-9.5 4-9.5 9.3 0 6.6 9.5 16.7 9.5 16.7s9.5-10.1 9.5-16.7C31.5 13 27.5 9 22 9z" fill="#2d6a12"/>
        <circle cx="22" cy="18.5" r="3.8" fill="#ffffff"/>
      </svg>
      <span>918 Pinchot Rd Larkfield, NH 02913</span>
    </div>
  </div>
</body>
</html>
```